Attorney Website Design

I need a top quality attorney website layout designed. Here are some examples of what I feel are great websites:
http://www.brelmoradivorceattorney.example/
http://www.vethomirlawfirm.example/
http://www.plexfirm.example/
http://www.harrowgatecriminaldefensefirm.example/
http://www.qzfirm.example/
http://www.tolvermoorcriminaldefensefirm.example/
http://www.drennocriminalattorneys.example/
http://www.qzfirm.example/
What we like about these sites:
• The different layers
• Subtle designs, textures, curves
• 3 dimensional
• Floating effects
• Prominent phone number
• Location of Areas of Practice
• Request A Consultation Prominent
• Right side bar with practice areas
• Badges
• Clear Calls to Action
• Dynamic/Staying Top navigation when you scroll
The project will be for a home page and then also an interior page (should be similar to home page).
I want to make it understood I am looking for a design which is not a typical "template" site which I can find anywhere for $50. This budget and project is for a "Custom" website design. Please submit designs similar in quality to the samples links I have posted. Creativity is a MUST! The best way to explain this is, I want a design that I can feel it unique and original, not something that looks like 95% of all websites out there.
Owen
I just wanted everyone to know that so far I am not to pleased with any of the designs. I am not looking for cut/pasting of other peoples websites but ORIGINAL and CREATIVE work.
Industry/Entity Type
Attorney

```html
<!DOCTYPE html>
<html lang="en">
<head>
<meta charset="utf-8">
<title>Tolvermoor Attorneys</title>
<link href="https://fonts.googleapis.com/css2?family=Arimo:wght@400;700&family=Cinzel:wght@400;600&family=Oswald:wght@600;700&display=swap" rel="stylesheet">
<style>
:root{
  --ink:#222;
  --brown:#8a3c1c;
  --header:#1b1b1b;
  --panel:#ececec;
  --white:#fff;
  --body-text:#555;
  --title:#555;
  --row:#dedede;
  --footer:#0a0a0a;
}
*{box-sizing:border-box;margin:0;padding:0}
html,body{width:758px;height:1200px;overflow:hidden}
body{position:relative;font-family:Arimo,Arial,sans-serif;color:var(--ink);background:var(--white)}
.abs{position:absolute}

.site-header{left:0;top:0;width:758px;height:75px;background:linear-gradient(#262626,#141414)}
.brand{left:64px;top:12px;width:200px;color:var(--white);text-align:center}
.brand-name{font-family:Cinzel,serif;font-size:27px;letter-spacing:.5px;line-height:32px;border-bottom:1px solid #888;padding-bottom:2px}
.brand-sub{font-size:11px;letter-spacing:9px;margin-top:4px;padding-left:8px}
.call{left:554px;top:16px;color:#ddd;display:flex;gap:6px;align-items:center}
.call small{display:block;font-size:8px}
.call strong{display:block;font-size:15px;font-weight:400;line-height:15px}
.nav{left:320px;top:50px;display:flex;font-size:9px}
.nav a{color:var(--white);text-decoration:none;height:19px;line-height:19px;padding:0 10px;margin-right:17px}
.nav a.active{background:var(--brown);border-radius:3px}

.hero{left:0;top:75px;width:758px;height:343px;background:linear-gradient(180deg,#8d8579 0%,#5a5650 45%,#2b2c2e 100%)}
.hero-person{left:50px;top:88px;width:230px;height:330px;background:radial-gradient(ellipse 60% 75% at 50% 65%,rgba(20,18,18,.95) 0%,rgba(30,28,28,.75) 55%,rgba(40,38,36,0) 100%)}
.hero-gavel{left:520px;top:285px;width:185px;height:133px;background:radial-gradient(ellipse 55% 60% at 50% 60%,rgba(140,80,35,.95) 0%,rgba(100,55,25,.7) 55%,rgba(60,40,30,0) 100%)}
.hero-title{left:284px;top:152px;font-family:Oswald,sans-serif;font-weight:700;font-size:34px;line-height:42px;color:var(--white);text-shadow:2px 2px 3px #000}
.hero-text{left:285px;top:253px;width:340px;font-size:9px;line-height:15.3px;color:var(--white);font-weight:700}

.consult{left:0;top:418px;width:758px;height:220px;background:var(--panel)}
.section-title{font-family:Cinzel,serif;font-weight:600;color:var(--brown);font-size:18.5px}
.field{background:var(--white);border:1px solid #ccc;border-radius:8px;display:flex;align-items:center;gap:6px;padding-left:6px;font-size:9px;color:#444}
.submit{left:586px;top:596px;width:88px;height:26px;background:var(--brown);color:var(--white);font-family:Oswald,sans-serif;font-size:14px;letter-spacing:.5px;text-align:center;line-height:26px}

.feature-title{font-family:Cinzel,serif;font-weight:600;font-size:17px;letter-spacing:1.5px;color:var(--title);text-align:center;width:194px}
.feature-img{width:194px;height:82px;border:4px solid var(--white);box-shadow:0 0 3px #aaa}
.feature-text{width:190px;font-size:7.6px;line-height:11.5px;color:var(--body-text);text-align:justify}
.more{width:64px;height:21px;background:var(--brown);color:var(--white);font-size:10px;text-align:center;line-height:21px}

.lower{left:0;top:896px;width:758px;height:228px;background:var(--panel)}
.lower-title{font-family:Cinzel,serif;font-weight:600;font-size:17px;letter-spacing:1.5px;color:var(--title)}
.divider{width:1px;height:180px;background:#d6d6d6}
.date{width:36px;height:42px;background:var(--brown);color:var(--white);text-align:center}
.date b{display:block;font-size:17px;line-height:22px}
.date span{display:block;font-size:11px}
.news-head{font-size:9.5px;color:var(--brown)}
.news-text{width:130px;font-size:8px;line-height:11.3px;color:var(--ink);text-align:justify}
.quote{left:272px;top:950px;width:186px;font-size:8px;line-height:11.4px;text-align:justify}
.practice{left:495px;top:946px;width:200px}
.practice li{list-style:none;height:27px;font-size:8.5px;padding:0 18px 0 19px;background:var(--row);border-bottom:1px solid #f4f4f4;display:flex;justify-content:space-between;align-items:center}
.practice li:nth-child(even){background:#ebebeb}
.plus{width:10px;height:10px;border-radius:50%;background:#111;color:#fff;font-size:9px;line-height:10px;text-align:center}

.footer-fade{left:250px;top:1108px;width:262px;height:16px;background:linear-gradient(rgba(10,10,10,0),var(--footer))}
.site-footer{left:0;top:1124px;width:758px;height:76px;background:var(--footer)}
.foot-links{left:65px;top:1152px;font-size:7.5px;color:#eee}
.copy{left:65px;top:1174px;font-size:7.5px;color:#eee}
.social{left:316px;top:1158px;display:flex;gap:9px}
.social span{width:21px;height:21px;border-radius:50%;background:radial-gradient(#bbb,#666);border:1px solid #333}
.newsletter{left:509px;top:1158px;width:175px;height:20px;display:flex}
.newsletter .in{flex:1;background:var(--white);font-size:7px;color:#666;line-height:20px;padding-left:6px}
.newsletter .go{width:22px;background:var(--brown);color:var(--white);font-size:8.5px;font-weight:700;text-align:center;line-height:20px;border:1px solid #ccc}
</style>
</head>
<body>

<header class="abs site-header">
  <div class="abs brand"><div class="brand-name">TOLVERMOOR</div><div class="brand-sub">ATTORNEYS</div></div>
  <div class="abs call">
    <svg width="16" height="16" viewBox="0 0 24 24"><path fill="#ccc" d="M6.6 10.8a15 15 0 0 0 6.6 6.6l2.2-2.2c.3-.3.7-.4 1-.2 1.1.4 2.3.6 3.6.6.6 0 1 .4 1 1V20c0 .6-.4 1-1 1A17 17 0 0 1 3 4c0-.6.4-1 1-1h3.5c.6 0 1 .4 1 1 0 1.3.2 2.5.6 3.6.1.3 0 .7-.2 1z"/></svg>
    <div><small>Call Now Today</small><strong>+7 (495) 555-01-47</strong></div>
  </div>
  <nav class="abs nav"><a class="active">HOME</a><a>ATTORNEY</a><a>FAQ'S</a><a>FAMILY LAW</a><a>CONTACT US</a></nav>
</header>

<section class="abs hero" role="img" aria-label="Blurred city skyline at sunset"></section>
<div class="abs hero-person" role="img" aria-label="Attorney in dark suit with arms crossed"></div>
<div class="abs hero-gavel" role="img" aria-label="Wooden gavel on a block marked law"></div>
<h1 class="abs hero-title">SEARCH NO MORE FOR<br>PERSONALIZED ADVICE</h1>
<p class="abs hero-text">Lorem ipsum dolor sit amet, consectetur adipisicing elit, sed do eiusmod tempor incididunt ut labore et dolore magna aliqua.sit amet, consectetur adip-isicing elit, sed do eiusmod tempor.</p>

<section class="abs consult"></section>
<h2 class="abs section-title" style="left:74px;top:436px">Request Free Consultation</h2>
<div class="abs field" style="left:72px;top:472px;width:182px;height:33px">
  <svg width="20" height="20" viewBox="0 0 20 20"><circle cx="10" cy="6" r="5" fill="#222"/><path d="M1 20c0-6 4-8 9-8s9 2 9 8z" fill="#222"/></svg>NAME</div>
<div class="abs field" style="left:286px;top:472px;width:183px;height:33px">
  <svg width="24" height="16" viewBox="0 0 24 16"><rect x="1" y="1" width="22" height="14" fill="none" stroke="#222" stroke-width="2"/><path d="M1 1l11 8 11-8M1 15l8-7M23 15l-8-7" fill="none" stroke="#222" stroke-width="1.6"/></svg>EMAIL</div>
<div class="abs field" style="left:498px;top:472px;width:182px;height:33px">
  <svg width="20" height="18" viewBox="0 0 20 18"><path d="M1 6c0-4 18-4 18 0v2h-5V6H6v2H1z" fill="#222"/><path d="M4 9h12l3 8H1z" fill="#222"/><circle cx="10" cy="13" r="2.5" fill="#fff"/></svg>PHONE</div>
<div class="abs field" style="left:72px;top:516px;width:609px;height:60px;align-items:flex-start;padding-top:6px">
  <svg width="26" height="22" viewBox="0 0 26 22"><path d="M2 2h22v13H10l-6 5v-5H2z" fill="#222"/><circle cx="9" cy="7" r="1.3" fill="#fff"/><circle cx="17" cy="7" r="1.3" fill="#fff"/><path d="M8 10q5 3 10 0" stroke="#fff" fill="none"/></svg><span style="margin-top:10px;margin-left:2px;font-size:8.5px">DESCRIBE YOUR CASE</span></div>
<div class="abs submit">SUBMIT</div>

<h3 class="abs feature-title" style="left:56px;top:664px">STANDARDS</h3>
<h3 class="abs feature-title" style="left:281px;top:664px">STAFF</h3>
<h3 class="abs feature-title" style="left:496px;top:664px">EXPERIENCE</h3>
<div class="abs feature-img" role="img" aria-label="Gavel and scales in warm light" style="left:64px;top:698px;background:linear-gradient(90deg,#e07a1c,#7a2a08)"></div>
<div class="abs feature-img" role="img" aria-label="Group of legal staff" style="left:280px;top:698px;background:linear-gradient(#d8d6d4,#3a3a3c)"></div>
<div class="abs feature-img" role="img" aria-label="Law books with a gavel" style="left:499px;top:698px;background:linear-gradient(90deg,#4a4636,#7a3a18)"></div>
<p class="abs feature-text" style="left:67px;top:791px">Lorem ipsum dolor sit amet, consectetur adipisic-ing elit, sed do eiusmod temporutmagna aliqua. enim ad minim veniam,nostrud exercitation ullamco laboris nisi ut aliquip ex.</p>
<p class="abs feature-text" style="left:284px;top:791px">Lorem ipsum dolor sit amet, consectetur adipisic-ing elit, sed do eiusmod temporutmagna aliqua. enim ad minim veniam,nostrud exercitation ullamco laboris nisi ut aliquip ex.</p>
<p class="abs feature-text" style="left:501px;top:791px">Lorem ipsum dolor sit amet, consectetur adipisic-ing elit, sed do eiusmod temporutmagna aliqua. enim ad minim veniam,nostrud exercitation ullamco laboris nisi ut aliquip ex.</p>
<div class="abs more" style="left:130px;top:850px">MORE</div>
<div class="abs more" style="left:351px;top:850px">MORE</div>
<div class="abs more" style="left:559px;top:850px">MORE</div>

<section class="abs lower"></section>
<h3 class="abs lower-title" style="left:66px;top:908px">LATEST NEWS</h3>
<h3 class="abs lower-title" style="left:293px;top:908px">TESTIMONIAL</h3>
<h3 class="abs lower-title" style="left:515px;top:908px">AREAS OF PRACTICE</h3>
<div class="abs divider" style="left:252px;top:926px"></div>
<div class="abs divider" style="left:476px;top:926px"></div>

<div class="abs date" style="left:56px;top:947px"><b>12</b><span>Jun</span></div>
<div class="abs news-head" style="left:100px;top:947px">Lorem ipsum</div>
<p class="abs news-text" style="left:100px;top:961px">Lorem ipsum dolor sit amet, con-sectetur adipisicing elit, sed do eiusmod dolore magna aliqua. Ut enim ad minim veniam,</p>
<div class="abs date" style="left:56px;top:1021px"><b>18</b><span>Mar</span></div>
<div class="abs news-head" style="left:101px;top:1021px">Lorem ipsum</div>
<p class="abs news-text" style="left:101px;top:1036px">Lorem ipsum dolor sit amet, con-sectetur adipisicing elit, sed do eiusmod dolore magna aliqua. Ut enim ad minim veniam,</p>

<p class="abs quote"><b style="font-size:14px;line-height:8px">&ldquo;</b> Lorem ipsum dolor sit amet, consectetur adipisicing elit, sed do eiusmod tempor incidi-dunt ut labore et dolore magna aliqua. Ut enim ad minim veniam, quis nostrud exercitation ullamco laboris nisi ut aliquip ex ea commodo consequat.Duis aute irure dolor in reprehenderit in voluptate velit esse cillum dolore eu fugiat nulla pariatur. Excepteur sint occaecat cupidatat non proident,<b style="font-size:14px;line-height:8px">&rdquo;</b></p>

<ul class="abs practice">
  <li>Driving Under the Influence<span class="plus">+</span></li>
  <li>Criminal Law Info<span class="plus">+</span></li>
  <li>Types Of Crimes<span class="plus">+</span></li>
  <li>Drug Crimes<span class="plus">+</span></li>
  <li>Sex Crimes<span class="plus">+</span></li>
</ul>

<div class="abs footer-fade" role="img" aria-label="Dark city skyline silhouette"></div>
<footer class="abs site-footer"></footer>
<div class="abs foot-links">O NAS | INDYWIDUALNI | KORPORACYJNI | KONTAKT</div>
<div class="abs copy">&copy; 2014 Tolvermoor Law. All Rights Reserved</div>
<div class="abs social"><span></span><span></span><span></span><span></span><span></span></div>
<div class="abs newsletter"><div class="in">Sign up to our newsletter</div><div class="go">GO</div></div>

</body>
</html>
```